Natural Skincare Product Labels Design

We are looking for a designer to create elegant but quirky, functional product labels for our natural skincare range.
The labels must reflect our brand’s values of simplicity, luxury, and the natural, handmade essence of our products.
https://www.pictogrove.com/marvellaskincare
1. Key Details
Packaging Dimensions
Container Types: Transparent jars.
Sizes for Body Products:
Diameter: 64mm–68mm.
Heights: 80mm, 88mm, and 97mm (lid height: 15mm).
Sizes for Face Creams:
Diameter: 60mm.
Height: 50mm (lid height: 15mm).
Label Fit: For body products, ideally one label size to fit all jar sizes.
For the smaller face cream jars, a separate, tailored label is required.
2. Label Placement
Options include a wrapped-around label or a combination of wrapped-around and top-of-jar elements.
Transparent jars mean the label must leave space for the product to be visible (e.g., partial wrap or cutout areas).
3. Content Requirements
Product Name: Prominently displayed.
Ingredient List: Dedicated space required.
Disclaimer/Usage Instructions: Include space for this information.
4. Design Goals
Look & Feel: Simple, upmarket, and natural, with a handmade essence.
Logo Usage: Our logo is finalized and available in gold, black, and white variants. Use Josefin Bold font for the logo if adjustments are required.
Color Palette: Neutral tones (e.g., whites, blacks, golds) are preferred, with flexibility for subtle pops of color tied to each product’s main ingredient.
5. Imagery
Open to including images and colours (e.g., botanical illustrations) that highlight the main ingredient (e.g., coffee beans, turmeric root, or honeycomb). Also open to labels having a prominent colour to tie it in to the main ingredient.
Alternatively, no images can also work for a clean design.
6. Current Design Context
Our temporary design features gold leaf on top and a simple handmade side label. We’re seeking to elevate this to a more polished, cohesive design.
7. Product Line
- Body Products (Larger Jars)
Tolo Body Butter
Key Ingredients: Guarana & Cupuaçu butter (inspired by Brazil).
Note: “Tolo” is slang for “bum.”
Manuka Honey Body Butter
Key Ingredients: Manuka honey (from New Zealand) & Cupuaçu butter.
Coffee Body Scrub
Key Ingredients: Coffee and Demerara sugar.
Whipped Body Soap - Turmeric
Key Ingredients: Turmeric and Bentonite clay.
Whipped Body Soap - Banana
- Face Products (Smaller Jars)
Face Cream
Key Ingredients: Carrot Oil and Raspberry Oil.
Features natural UV protection.
Good Night Cream
Key Ingredients: Enriched with Magnesium.
Promotes relaxation and restful sleep.
8. Submission Guidelines
Flexibility: Design should allow for consistent branding across all products while accommodating the varying jar sizes and ingredient focus.
Material Considerations: Labels should complement the transparent jars and allow the product inside to remain partially visible.
Print Elements: Incorporating gold accents is a plus but should not overpower the design.
We’re excited to see your vision for a label that celebrates the natural beauty and high quality of our skincare range. Please include mockups to showcase the design in use, particularly on transparent jars of varying sizes.
women 20-50 years of age

```html
<!DOCTYPE html>
<html lang="en">
<head>
<meta charset="utf-8">
<title>Marvella Natural Skincare – Labels</title>
<link href="https://fonts.googleapis.com/css2?family=DM+Serif+Display&family=Josefin+Sans:wght@400;600;700&family=Jost:wght@400&display=swap" rel="stylesheet">
<style>
  :root{
    --bg:#ffffff;
    --gold-light:#d9b277;
    --gold-dark:#a27c56;
    --espresso:#5a3a1c;
    --bean:#6b4522;
    --cream:#f4e7cf;
    --amp:#e6cd98;
    --ink:#6b4a2c;
    --pink-light:#ecc8cf;
    --pink-dark:#d39eaa;
    --plum:#8c5964;
    --plum-soft:#9b6b74;
    --lid:#242424;
    --lid-line:#d9cdbd;
  }
  *{margin:0;padding:0;box-sizing:border-box}
  html,body{width:1200px;height:968px;overflow:hidden;background:var(--bg)}
  .canvas{position:relative;width:1200px;height:968px}

  .label{position:absolute}
  .label__shape{position:absolute;inset:0;width:100%;height:100%}

  /* coffee scrub label */
  .label--coffee{left:67px;top:71px;width:1063px;height:336px}
  .ingredients,.how-to{position:absolute;font-family:"Josefin Sans",sans-serif;font-weight:600;font-size:12px;line-height:17px;color:var(--ink);letter-spacing:.2px;text-transform:uppercase}
  .ingredients{left:57px;top:74px;width:200px}
  .how-to{left:805px;top:66px;width:180px}
  .badges{position:absolute;left:57px;top:176px;display:flex;gap:10px}
  .badge{width:54px;height:54px;border:1.4px solid var(--ink);border-radius:50%;opacity:.85}

  .tag{position:absolute;font-family:"Josefin Sans",sans-serif;font-weight:400;letter-spacing:2px;color:var(--cream);text-transform:uppercase;line-height:1}
  .label--coffee .tag{left:341px;top:68px;font-size:15px}
  .name{position:absolute;font-family:"DM Serif Display",serif;line-height:1;white-space:nowrap}
  .name--coffee{left:333px;top:96px;font-size:78px;color:var(--espresso);letter-spacing:-1px}
  .name--amp{left:332px;top:156px;font-size:96px;color:var(--amp)}
  .name--demerara{left:389px;top:153px;font-size:54px;color:var(--bean);letter-spacing:-.5px}
  .name--sugar{left:411px;top:189px;font-size:54px;color:var(--bean)}
  .product-type{position:absolute;font-family:"Josefin Sans",sans-serif;font-weight:700;letter-spacing:3.2px;color:#fff;text-transform:uppercase;line-height:1}
  .label--coffee .product-type{left:340px;top:257px;font-size:18px}
  .size{position:absolute;font-family:"Jost",sans-serif;font-size:14px;line-height:19px;color:var(--ink);text-align:right}
  .label--coffee .size{left:545px;top:258px;width:140px}

  .brand-seal{position:absolute;display:flex;align-items:center;justify-content:center;border:1.4px solid var(--cream);border-radius:50%}
  .brand-seal span{font-family:"Josefin Sans",sans-serif;font-weight:700;letter-spacing:3px;color:var(--cream)}
  .label--coffee .brand-seal{left:554px;top:24px;width:168px;height:168px}
  .label--coffee .brand-seal span{font-size:19px}

  .botanical{position:absolute;left:721px;top:143px;width:126px;height:190px;border-radius:50% 50% 40% 40%;background:linear-gradient(160deg,rgba(244,231,207,.28),rgba(244,231,207,.08))}

  /* tolo body butter label */
  .label--tolo{left:67px;top:470px;width:540px;height:320px}
  .label--tolo .tag{left:48px;top:60px;font-size:12px}
  .name--tolo{left:46px;top:80px;font-size:66px;color:var(--plum)}
  .name--cream{left:100px;top:138px;font-size:58px;color:var(--plum-soft)}
  .ingredient-line{position:absolute;left:48px;top:207px;font-family:"Jost",sans-serif;font-size:15px;color:var(--plum-soft);letter-spacing:.3px}
  .label--tolo .product-type{left:47px;top:240px;font-size:16px}
  .label--tolo .size{left:330px;top:244px;width:140px;color:var(--plum)}
  .label--tolo .brand-seal{left:360px;top:30px;width:140px;height:140px}
  .label--tolo .brand-seal span{font-size:16px}

  /* lid top */
  .lid{position:absolute;left:752px;top:546px;width:326px;height:326px;border-radius:50%;background:var(--lid);display:flex;align-items:center;justify-content:center}
  .lid .brand-seal{position:static;width:200px;height:200px;border-color:var(--lid-line)}
  .lid .brand-seal span{font-size:22px;color:var(--lid-line)}
</style>
</head>
<body>
<main class="canvas">

  <section class="label label--coffee" aria-label="Coffee and demerara sugar body scrub label">
    <svg class="label__shape" viewBox="0 0 1063 336" preserveAspectRatio="none" aria-hidden="true">
      <defs>
        <linearGradient id="goldFill" x1="0" y1="0" x2="1" y2="1">
          <stop offset="0" stop-color="var(--gold-light)"/>
          <stop offset=".4" stop-color="#d2aa74"/>
          <stop offset="1" stop-color="var(--gold-dark)"/>
        </linearGradient>
      </defs>
      <path fill="url(#goldFill)" d="M0 0H1063V296C1052 322 1020 332 995 318C960 298 925 294 890 310C850 330 810 330 760 320C700 308 640 300 580 316C540 326 500 316 485 303C460 282 430 280 400 287C350 300 300 312 250 318C200 324 180 300 150 312C110 328 80 314 50 314C20 316 5 310 0 300Z"/>
    </svg>

    <p class="ingredients">Ingredients:<br>Coconut butter, cocoa butter, vanilla fragance, coffee, demarara sugar, vitamin E</p>
    <div class="badges" aria-hidden="true"><span class="badge"></span><span class="badge"></span><span class="badge"></span></div>

    <p class="tag">100% Organic</p>
    <span class="name name--amp" aria-hidden="true">&amp;</span>
    <h1 class="name name--coffee">coffee</h1>
    <span class="name name--demerara">demerara</span>
    <span class="name name--sugar">sugar</span>
    <p class="product-type">Body Scrub</p>
    <p class="size">Whipped butter<br>2 OZ / 60ML</p>

    <div class="brand-seal"><span>MARVELLA</span></div>
    <div class="botanical" role="img" aria-label="Fine line botanical leaf sprig illustration"></div>

    <p class="how-to">How to use<br>Shake well before use.<br>Apply to skin and/or hair and massage well</p>
  </section>

  <section class="label label--tolo" aria-label="Tolo body butter label">
    <svg class="label__shape" viewBox="0 0 540 320" preserveAspectRatio="none" aria-hidden="true">
      <defs>
        <linearGradient id="pinkFill" x1="0" y1="0" x2="1" y2="1">
          <stop offset="0" stop-color="var(--pink-light)"/>
          <stop offset="1" stop-color="var(--pink-dark)"/>
        </linearGradient>
      </defs>
      <path fill="url(#pinkFill)" d="M0 0H540V300C515 314 490 296 460 292C420 287 390 306 350 310C300 314 260 280 220 278C180 276 150 302 110 304C70 306 40 284 0 292Z"/>
    </svg>
    <p class="tag">100% Organic</p>
    <h2 class="name name--tolo">tolo</h2>
    <span class="name name--cream">cream</span>
    <p class="ingredient-line">guarana &amp; cupuaçu butter</p>
    <p class="product-type">Body Butter</p>
    <p class="size">Whipped butter<br>2 OZ / 60ML</p>
    <div class="brand-seal"><span>MARVELLA</span></div>
  </section>

  <section class="lid" aria-label="Jar lid top">
    <div class="brand-seal"><span>MARVELLA</span></div>
  </section>

</main>
</body>
</html>
```